mortgage company professional business card

We would like to revamp our business card. Logos and current card attached.

Target Market(s)

white collar professionals

Industry/Entity Type

Mortgage Lender

Contact Information for Business Card

Looking for a sharp professional feel with white background for business card. No gloss. Looking for emboss.

Requirements
Must have
• -Professional touch
• -Emboss and raised lettering
• -Social media icons
• name, title, Phone, email, NMLS and web
• Complement logo and web

```html
<!DOCTYPE html>
<html lang="en">
<head>
<meta charset="utf-8">
<title>Lendwell – Business Card</title>
<link href="https://fonts.googleapis.com/css2?family=Josefin+Sans:wght@600;700&family=Questrial&display=swap" rel="stylesheet">
<style>
  :root {
    --navy: #2d3052;
    --green: #3b9a3e;
    --text: #4a4c5e;
    --card: #ffffff;
    --backdrop: #e9e9ec;
  }
  * { margin: 0; padding: 0; box-sizing: border-box; }
  html, body {
    width: 1200px; height: 1047px; overflow: hidden;
    background: var(--backdrop);
    font-family: "Questrial", sans-serif;
  }
  .card {
    position: absolute; left: 60px; top: 230px;
    width: 1080px; height: 586px;
    background: var(--card);
    border-radius: 18px;
    overflow: hidden;
    box-shadow: 0 10px 30px rgba(0,0,0,.12);
  }
  .brand-mark {
    position: absolute; left: 74px; top: 186px;
    width: 40px; height: 40px; background: var(--navy);
  }
  .brand-name {
    position: absolute; left: 128px; top: 170px;
    font-family: "Questrial", sans-serif;
    font-size: 54px; line-height: 1; color: var(--navy);
    letter-spacing: 0.5px;
  }
  .tagline {
    position: absolute; left: 128px; top: 232px;
    font-size: 21px; color: var(--text);
  }
  .person-name {
    position: absolute; right: 47px; top: 262px;
    font-family: "Josefin Sans", sans-serif; font-weight: 700;
    font-size: 42px; line-height: 1; color: var(--navy);
    letter-spacing: 1.5px;
  }
  .person-title {
    position: absolute; right: 47px; top: 312px;
    font-size: 23px; line-height: 1; color: var(--green);
    letter-spacing: 0.5px;
  }
  .accent-green { position: absolute; left: 1055px; top: 271px; width: 5px; height: 69px; background: var(--green); }
  .accent-navy { position: absolute; left: 1066px; top: 271px; width: 14px; height: 69px; background: var(--navy); }
  .divider { position: absolute; left: 55px; top: 328px; width: 732px; height: 2px; background: var(--green); }
  .contact-list { position: absolute; left: 57px; top: 368px; list-style: none; }
  .contact-list li {
    display: flex; align-items: center; gap: 12px;
    height: 32.5px; font-size: 25px; color: var(--text);
  }
  .contact-list svg { width: 16px; height: 16px; flex: none; }
  .address {
    position: absolute; left: 57px; top: 476px;
    font-size: 25px; line-height: 33px; color: var(--text);
  }
  .bands { position: absolute; left: 0; top: 0; width: 1080px; height: 586px; }
</style>
</head>
<body>
  <div class="card">
    <div class="brand-mark"></div>
    <div class="brand-name">Lendwell</div>
    <div class="tagline">Home loans made clear.</div>

    <div class="person-name">DANIEL REEVE</div>
    <div class="person-title">Managing Director</div>
    <div class="accent-green"></div>
    <div class="accent-navy"></div>
    <div class="divider"></div>

    <ul class="contact-list">
      <li>
        <svg viewBox="0 0 16 16"><path fill="var(--green)" d="M3.5 1.5l2.5 0 1 3.5-1.8 1.2a8 8 0 0 0 4.6 4.6L11 9l3.5 1v2.5c0 1-1 2-2 2A11 11 0 0 1 1.5 3.5c0-1 1-2 2-2z"/></svg>
        0800 (555) 0192
      </li>
      <li>
        <svg viewBox="0 0 16 16"><rect x="1.5" y="3.5" width="13" height="9" fill="none" stroke="var(--green)" stroke-width="1.6"/><path d="M1.5 3.5 8 9l6.5-5.5" fill="none" stroke="var(--green)" stroke-width="1.6"/></svg>
        info@lendwellhome.com
      </li>
      <li>
        <svg viewBox="0 0 16 16"><circle cx="8" cy="8" r="6.5" fill="none" stroke="var(--green)" stroke-width="1.4"/><ellipse cx="8" cy="8" rx="2.8" ry="6.5" fill="none" stroke="var(--green)" stroke-width="1.2"/><path d="M1.5 8h13M2.5 5h11M2.5 11h11" stroke="var(--green)" stroke-width="1.1"/></svg>
        www.lendwellhome.com
      </li>
    </ul>

    <p class="address">12345 Address Street City State<br>Postcode Country</p>

    <svg class="bands" viewBox="0 0 1080 586" aria-hidden="true">
      <polygon points="0,565 561,565 553,586 0,586" fill="var(--green)"/>
      <polygon points="629,514 1080,514 1080,586 555,586" fill="var(--navy)"/>
    </svg>
  </div>
</body>
</html>
```